Small Salsa business needs web design + coding

LA Brisa Verde is a small business started in Pocatello, Idaho and is looking to expand online. We focus on keeping the salsa all natural and more about savor than spiciness. Similar to the photo we've attached of just one of our salsas, we want a website that is friendly for users of all ages to use, as well as advertising in the website, and offer online shopping. Other things you think is beneficial to a small business like ours, proposals are welcomed and encouraged. We would also like to be able to remove and add stuff as we continue to grow our business.

Coding

```html
<!DOCTYPE html>
<html lang="en">
<head>
<meta charset="utf-8">
<title>LA Brisa Verde — Salsa Casera</title>
<link rel="stylesheet" href="https://fonts.googleapis.com/css2?family=Playfair+Display:wght@400&family=Roboto:wght@400;500;700&family=Poppins:wght@400;500;600&display=swap">
<style>
:root{
  --red:#e1141c;
  --ink:#1f1f1f;
  --muted:#5a5a5a;
  --tan:#c9a47c;
  --tan-dark:#a8804f;
  --brown:#7a4d25;
  --topbar:#6e4522;
  --white:#fff;
}
*{box-sizing:border-box;margin:0;padding:0}
html,body{width:1200px;height:3865px;overflow:hidden}
body{position:relative;background:var(--white);font-family:'Roboto',sans-serif;color:var(--ink)}
.abs{position:absolute}
.serif{font-family:'Playfair Display',serif;font-weight:400}
.btn{position:absolute;display:flex;align-items:center;justify-content:center;color:#fff;font-weight:700;font-size:16px;background:var(--ink)}
.btn.red{background:var(--red)}

/* top bar */
.topbar{left:0;top:0;width:1200px;height:47px;background:var(--topbar);color:#fff;font-size:12.5px;font-weight:500}
.topbar .promo{left:112px;top:15px}
.topbar .promo u{color:#e7b98f}
.topbar .links{right:110px;top:15px;display:flex;gap:14px}

/* hero */
.hero{left:0;top:47px;width:1200px;height:680px;background:radial-gradient(ellipse at 70% 40%,#8a6a3a 0%,#5a3d20 45%,#2d1d10 100%)}
.hero-jar{left:110px;top:230px;width:300px;height:400px;border-radius:40px 40px 30px 30px;background:linear-gradient(#9aa0a4,#7c5c34 25%,#8a3e24 60%,#5a7a3a)}
.logo{left:112px;top:62px;display:flex;align-items:center;gap:8px;color:#fff;font-size:17px;font-weight:500}
.logo i{width:12px;height:12px;border-radius:50%;background:#fff;display:block}
.nav{left:340px;top:93px;display:flex;gap:18px;color:#fff;font-size:15.5px;font-weight:500}
.nav .on{border-bottom:2px solid #fff}
.nav-icons{left:1012px;top:88px;display:flex;gap:22px}
.hero-kicker{left:504px;top:282px;color:#fff;font-size:18px;font-weight:500}
.hero-title{left:504px;top:308px;color:#fff;font-family:'Poppins',sans-serif;font-weight:600;font-size:44px;line-height:64px;white-space:nowrap}
.hero-copy{left:504px;top:370px;width:580px;color:#fff;font-family:'Poppins',sans-serif;font-size:17px;line-height:30px}
.hero-curve{left:0;top:600px}

/* products */
.section-title{left:0;width:1200px;text-align:center;font-size:41px}
.product{width:250px;text-align:center}
.product .jar{margin:0 auto;width:150px;height:240px;border-radius:26px 26px 18px 18px;background:linear-gradient(#a9adb0 0%,#8a8f92 14%,#9a5a34 30%,#8c3a24 65%,#5d7b3c 100%)}
.product .jar.yellow{background:linear-gradient(#a9adb0 0%,#8a8f92 14%,#c9b24a 30%,#d8c65a 65%,#6b8a3e 100%)}
.product .jar.orange{background:linear-gradient(#a9adb0 0%,#8a8f92 14%,#a8542a 30%,#c86a2a 65%,#7b3a20 100%)}
.product .name{font-size:14.5px;font-weight:500;margin-top:38px;white-space:nowrap}
.product .price{font-size:23px;font-weight:700;margin-top:10px}
.featured{left:360px;top:880px;width:228px;height:273px;background:#fff;box-shadow:0 2px 8px rgba(0,0,0,.2)}

/* natural */
.natural-photo{left:0;top:1380px;width:598px;height:382px;background:linear-gradient(#3f6a2c 0%,#4f7a36 30%,#9a6a3a 55%,#b0b4b6 100%)}
.body-copy{font-size:13.5px;line-height:28.5px;color:var(--muted)}

/* testimonials */
.quote-card{top:1915px;width:463px;height:226px;background:#fff;box-shadow:0 1px 8px rgba(0,0,0,.18)}
.quote-card .mark{left:28px;top:30px;color:var(--red);font-family:'Playfair Display',serif;font-size:52px;line-height:1}
.quote-card p{left:63px;top:34px;width:375px;font-size:15px;font-style:italic;line-height:26px;color:#444}
.quote-card .who{left:63px;top:148px;display:flex;align-items:center;gap:8px;font-size:15px}
.avatar{width:48px;height:48px;border-radius:50%;background:#6a6a6a}

/* more products */
.more{left:0;top:2228px;width:1200px;height:610px;background:linear-gradient(#3b2f26,#5a4634 50%,#3a2a1e)}
.more-card{top:2368px;width:274px;height:320px;background:#fff}
.more-card .jar{left:77px;top:22px;width:120px;height:170px;border-radius:22px 22px 16px 16px}
.more-card .name{left:0;top:226px;width:274px;text-align:center;font-size:15px;font-weight:500;white-space:nowrap}
.more-card .price{left:0;top:253px;width:274px;text-align:center;font-size:23px;font-weight:700}
.more-card .btn{left:50px;top:292px;width:174px;height:42px}
.more-card svg{position:absolute;left:245px}

/* about */
.about-title{left:111px;top:2994px;font-size:30px;white-space:nowrap}
.about-photo{left:600px;top:2925px;width:600px;height:453px;background:linear-gradient(#c8c9c4 0%,#8a8c84 30%,#4a4a3e 55%,#d9d2bf 75%,#3a3a34 100%)}

/* footer */
.footer{left:0;top:3435px;width:1200px;height:430px}
.feature{display:flex;align-items:center;gap:12px;font-family:'Poppins',sans-serif;font-size:16px;color:#fff}
.fcol h4{font-family:'Poppins',sans-serif;font-weight:600;font-size:17px;color:#fff;margin-bottom:12px}
.fcol p{font-size:12px;color:#fff;line-height:28.5px}
.copy{left:0;top:3800px;width:1200px;height:65px;background:var(--tan-dark)}
</style>
</head>
<body>

<div class="abs topbar">
  <div class="abs promo">Use code SUMMER10 for 10% off - <u>VIEW DEALS &gt;</u></div>
  <div class="abs links"><span>&#9679; HELP CENTER</span><span>|</span><span>TRACK ORDER</span><span>|</span><span>PAY ONLINE &amp; GET FREE SHIPPING.</span></div>
</div>

<div class="abs hero" role="img" aria-label="Plate of nachos and grilled meat beside a jar of salsa verde on a wooden table"></div>
<div class="abs hero-jar" role="img" aria-label="Jar of LA Brisa Verde salsa verde"></div>
<div class="abs logo"><i></i>LA Brisa Verde</div>
<nav class="abs nav">
  <span class="on">HOME</span><span>|</span><span>HOW TO USE IT</span><span>|</span><span>PRODUCTS</span><span>|</span><span>LEAVE US A REVIEW</span><span>|</span><span>CONTACT US</span>
</nav>
<div class="abs nav-icons">
  <svg width="28" height="28" viewBox="0 0 28 28" fill="none" stroke="#fff" stroke-width="2"><circle cx="14" cy="14" r="12"/><circle cx="14" cy="11" r="4"/><path d="M6 22c3-5 13-5 16 0"/></svg>
  <svg width="28" height="28" viewBox="0 0 28 28" fill="#fff"><path d="M2 5h4l3 12h13l3-9H8" stroke="#fff" stroke-width="2" fill="none"/><circle cx="11" cy="22" r="2"/><circle cx="20" cy="22" r="2"/><circle cx="24" cy="5" r="4" fill="var(--red)"/></svg>
</div>
<div class="abs hero-kicker">LA BRISA VERDE SALSA CASERA</div>
<h1 class="abs hero-title">ALL NATURAL INGREDIENTS</h1>
<p class="abs hero-copy">Lorem ipsum dolor sit amet, consectetur adipiscing elit, sed do eiusmod tempor incididunt ut labore et dolore magna aliqua.</p>
<div class="btn red" style="left:505px;top:447px;width:163px;height:50px;font-size:16px">ORDER NOW</div>
<svg class="abs hero-curve" width="1200" height="130" viewBox="0 0 1200 130">
  <path d="M0 20 Q600 150 1200 20 L1200 130 L0 130Z" fill="var(--tan)"/>
  <path d="M0 35 Q600 150 1200 35 L1200 130 L0 130Z" fill="#fff"/>
</svg>

<h2 class="abs section-title serif" style="top:795px">Our Products</h2>
<div class="abs featured"></div>
<div class="abs product" style="left:101px;top:900px"><div class="jar" role="img" aria-label="Jar of salsa verde"></div><div class="name">LA Brisa Verde Salsa Verde</div><div class="price">$6.99 per jar</div></div>
<div class="abs product" style="left:350px;top:900px"><div class="jar orange" role="img" aria-label="Jar of habanero salsa"></div><div class="name">LA Brisa Verde Crema de Serrano</div><div class="price">$6.99 per jar</div></div>
<div class="abs product" style="left:599px;top:900px"><div class="jar yellow" role="img" aria-label="Jar of crema de serrano"></div><div class="name">LA Brisa Verde Habanero</div><div class="price">$6.99 per jar</div></div>
<div class="abs product" style="left:849px;top:900px"><div class="jar" role="img" aria-label="Jar of salsa verde"></div><div class="name">LA Brisa Verde Habanero</div><div class="price">$6.99 per jar</div></div>
<div class="btn" style="left:139px;top:1252px;width:174px;height:42px">Add To Cart</div>
<div class="btn red" style="left:388px;top:1252px;width:174px;height:42px">Add To Cart</div>
<div class="btn" style="left:637px;top:1252px;width:174px;height:42px">Add To Cart</div>
<div class="btn" style="left:887px;top:1252px;width:174px;height:42px">Add To Cart</div>

<div class="abs natural-photo" role="img" aria-label="Four jars of salsa lined up in front of green leaves"></div>
<h2 class="abs serif" style="left:634px;top:1403px;font-size:44px">All Natural Ingredients</h2>
<p class="abs body-copy" style="left:634px;top:1470px;width:454px">Lorem ipsum dolor sit amet, consectetur adipiscing elit, sed do eiusmod tempor incididunt ut labore et dolore magna aliqua. Ut enim ad minim veniam, quis nostrud exercitation ullamco laboris nisi ut aliquip ex ea commodo consequat. Duis aute irure dolor in reprehenderit in voluptate velit esse cillum dolore eu fugiat nulla pariatur. Excepteur sint occaecat cupidatat non proident, sunt in culpa qui officia deserunt mollit anim id est laborum</p>
<div class="btn red" style="left:640px;top:1684px;width:174px;height:42px">Buy Now</div>

<h2 class="abs section-title serif" style="top:1832px">What Our Clients Say</h2>
<svg class="abs" style="left:68px;top:2012px" width="34" height="22" viewBox="0 0 34 22" fill="none" stroke="#222" stroke-width="2.5"><path d="M33 11H3M12 2 3 11l9 9"/></svg>
<svg class="abs" style="left:1098px;top:2012px" width="34" height="22" viewBox="0 0 34 22" fill="none" stroke="#222" stroke-width="2.5"><path d="M1 11h30M22 2l9 9-9 9"/></svg>
<div class="abs quote-card" style="left:123px">
  <div class="abs mark">&ldquo;</div>
  <p class="abs">Lorem ipsum dolor sit amet, consectetur adipiscing elit, sed do eiusmod tempor incididunt ut labore et dolore magna aliqua. Quis ipsum suspendisse ultrices gravida. Risu modo viverra maecenas</p>
  <div class="abs who"><div class="avatar" role="img" aria-label="Customer portrait"></div>- Marcus Hale</div>
</div>
<div class="abs quote-card" style="left:614px">
  <div class="abs mark">&ldquo;</div>
  <p class="abs">Lorem ipsum dolor sit amet, consectetur adipiscing elit, sed do eiusmod tempor incididunt ut labore et dolore magna aliqua. Quis ipsum suspendisse ultrices gravida. Risu modo viverra maecenas</p>
  <div class="abs who"><div class="avatar" role="img" aria-label="Customer portrait"></div>- Owen Pratt</div>
</div>

<div class="abs more" role="img" aria-label="Dim photo of a served plate of food"></div>
<svg class="abs" style="left:0;top:2730px" width="1200" height="110" viewBox="0 0 1200 110">
  <path d="M0 10 Q600 150 1200 10 L1200 110 L0 110Z" fill="var(--tan)"/>
  <path d="M0 25 Q600 150 1200 25 L1200 110 L0 110Z" fill="#fff"/>
</svg>
<h2 class="abs section-title serif" style="top:2272px;color:#fff;font-size:41px">More Products You May Like</h2>
<svg class="abs" style="left:110px;top:2512px" width="34" height="34" viewBox="0 0 34 34" fill="none" stroke="#fff" stroke-width="2"><circle cx="17" cy="17" r="15"/><path d="M25 17H9m6-6-6 6 6 6"/></svg>
<svg class="abs" style="left:1053px;top:2512px" width="34" height="34" viewBox="0 0 34 34" fill="none" stroke="#fff" stroke-width="2"><circle cx="17" cy="17" r="15"/><path d="M9 17h16m-6-6 6 6-6 6"/></svg>

<div class="abs more-card" style="left:160px">
  <div class="abs jar" style="background:linear-gradient(#a9adb0,#8a8f92 14%,#9a5a34 30%,#8c3a24 65%,#5d7b3c)" role="img" aria-label="Jar of salsa verde"></div>
  <svg style="top:14px" width="20" height="18" viewBox="0 0 20 18" fill="none" stroke="#999" stroke-width="1.4"><path d="M10 17S1 11 1 5.5A4.5 4.5 0 0 1 10 4a4.5 4.5 0 0 1 9 1.5C19 11 10 17 10 17Z"/></svg>
  <svg style="top:42px" width="20" height="20" viewBox="0 0 20 20" fill="none" stroke="#999" stroke-width="1.4"><circle cx="10" cy="10" r="8.5"/><path d="M10 9v5M10 6v1"/></svg>
  <div class="abs name">LA Brisa Verde Crema de Serrano</div><div class="abs price">$7.99 a jar</div>
  <div class="btn">Add To Cart</div>
</div>
<div class="abs more-card" style="left:461px">
  <div class="abs jar" style="background:linear-gradient(#a9adb0,#8a8f92 14%,#c9b24a 30%,#d8c65a 65%,#6b8a3e)" role="img" aria-label="Jar of crema de serrano"></div>
  <svg style="top:14px" width="20" height="18" viewBox="0 0 20 18" fill="none" stroke="#999" stroke-width="1.4"><path d="M10 17S1 11 1 5.5A4.5 4.5 0 0 1 10 4a4.5 4.5 0 0 1 9 1.5C19 11 10 17 10 17Z"/></svg>
  <svg style="top:42px" width="20" height="20" viewBox="0 0 20 20" fill="none" stroke="#999" stroke-width="1.4"><circle cx="10" cy="10" r="8.5"/><path d="M10 9v5M10 6v1"/></svg>
  <div class="abs name">LA Brisa Verde Crema de Serrano</div><div class="abs price">$7.99 a jar</div>
  <div class="btn red">Add To Cart</div>
</div>
<div class="abs more-card" style="left:761px">
  <div class="abs jar" style="background:linear-gradient(#a9adb0,#8a8f92 14%,#a8542a 30%,#c86a2a 65%,#7b3a20)" role="img" aria-label="Jar of habanero salsa"></div>
  <svg style="top:14px" width="20" height="18" viewBox="0 0 20 18" fill="none" stroke="#999" stroke-width="1.4"><path d="M10 17S1 11 1 5.5A4.5 4.5 0 0 1 10 4a4.5 4.5 0 0 1 9 1.5C19 11 10 17 10 17Z"/></svg>
  <svg style="top:42px" width="20" height="20" viewBox="0 0 20 20" fill="none" stroke="#999" stroke-width="1.4"><circle cx="10" cy="10" r="8.5"/><path d="M10 9v5M10 6v1"/></svg>
  <div class="abs name">LA Brisa Verde Crema de Serrano</div><div class="abs price">$7.99 a jar</div>
  <div class="btn">Add To Cart</div>
</div>

<h2 class="abs serif about-title">About LaBrisaVerde.salsa.casera.</h2>
<p class="abs body-copy" style="left:111px;top:3053px;width:445px">Lorem ipsum dolor sit amet, consectetur adipiscing elit, sed do eiusmod tempor incididunt ut labore et dolore magna aliqua. Ut enim ad minim veniam, quis nostrud exercitation ullamco laboris nisi ut aliquip ex ea commodo consequat. Duis aute irure dolor in reprehenderit in voluptate velit esse cillum dolore eu fugiat nulla pariatur. Excepteur sint occaecat cupidatat non proident, sunt in culpa qui officia deserunt mollit anim id est laborum</p>
<div class="btn red" style="left:111px;top:3267px;width:174px;height:42px">Learn More</div>
<div class="abs about-photo" role="img" aria-label="Breakfast plate with omelette and fruit beside a salsa jar and a coffee mug by a window"></div>

<svg class="abs footer" width="1200" height="430" viewBox="0 0 1200 430">
  <path d="M0 70 Q600 -40 1200 70 L1200 430 L0 430Z" fill="var(--tan-dark)"/>
  <path d="M0 80 Q600 -20 1200 80 L1200 430 L0 430Z" fill="var(--tan)"/>
  <line x1="112" y1="163" x2="1088" y2="163" stroke="#e5cfb6" stroke-width="1"/>
  <line x1="443" y1="75" x2="443" y2="135" stroke="#e5cfb6"/>
  <line x1="744" y1="75" x2="744" y2="135" stroke="#e5cfb6"/>
</svg>
<div class="abs feature" style="left:170px;top:3517px">
  <svg width="48" height="34" viewBox="0 0 48 34" fill="none" stroke="#fff" stroke-width="1.8"><rect x="2" y="6" width="28" height="18"/><path d="M30 12h9l6 7v5H30"/><circle cx="10" cy="27" r="4"/><circle cx="37" cy="27" r="4"/></svg>Free Shipping Available</div>
<div class="abs feature" style="left:472px;top:3513px">
  <svg width="36" height="42" viewBox="0 0 36 42" fill="none" stroke="#fff" stroke-width="1.8"><path d="M18 2 3 8v12c0 10 7 17 15 20 8-3 15-10 15-20V8Z"/><path d="m11 21 5 5 9-10"/></svg>Secure online payment</div>
<div class="abs feature" style="left:770px;top:3513px">
  <svg width="44" height="44" viewBox="0 0 44 44" fill="none" stroke="#fff" stroke-width="1.8"><path d="M4 12 20 4l16 8v18l-16 8-16-8Z"/><path d="M4 12l16 8 16-8M20 20v18"/><circle cx="33" cy="33" r="8"/><path d="m29 33 3 3 5-6"/></svg>Satisfaction Guaranteed</div>

<div class="abs fcol" style="left:113px;top:3608px"><h4>About Us</h4><p>Contact<br>About<br>How It Works<br>Help Center</p></div>
<div class="abs fcol" style="left:256px;top:3608px;width:320px"><h4>PURCHASING AND DISTRIBUTION</h4><p>If you would like to place a bulk order or are interested<br>in becoming a distributor of our products please feel free<br>&nbsp;to reach out &nbsp;via the following contact information.</p></div>
<div class="abs fcol" style="left:616px;top:3608px"><h4>info</h4><p>555 014 2290<br>info@labrisaverdesalsa.com<br>48 Cedar Lane Pocatello ID<br>83201</p></div>
<div class="abs fcol" style="left:848px;top:3608px"><h4>SUBSCRIBE TO OUR EMAIL</h4></div>
<div class="abs" style="left:848px;top:3648px;width:240px;height:40px;border-radius:20px;background:#fff;font-size:13px;color:#777;padding:12px 20px">Email</div>
<svg class="abs" style="left:1048px;top:3650px" width="36" height="36" viewBox="0 0 36 36"><circle cx="18" cy="18" r="18" fill="var(--red)"/><path d="M10 18 26 10l-5 17-4-6Z" fill="none" stroke="#fff" stroke-width="1.6"/></svg>
<div class="abs" style="left:848px;top:3708px;width:16px;height:20px;background:#fff"></div>
<div class="abs" style="left:876px;top:3708px;width:20px;height:20px;background:#fff"></div>

<div class="abs copy"></div>
<div class="abs" style="left:112px;top:3825px;color:#fff;font-size:13px">Copyright &copy; 2021. All Rights Reserved</div>
<div class="abs" style="left:577px;top:3828px;color:#fff;font-size:12px;display:flex;gap:28px"><span>How to use it</span><span>Leave us a review</span><span>More Products</span></div>
<div class="abs" style="left:928px;top:3805px;width:160px;height:48px;background:#fff;border-radius:3px;display:flex;flex-wrap:wrap;gap:4px;padding:6px;align-content:flex-start">
  <div style="width:44px;height:14px;background:#2a4a8a"></div>
  <div style="width:100%;height:0"></div>
  <div style="width:34px;height:18px;background:#1a3a8a"></div>
  <div style="width:28px;height:18px;background:#e8a23a"></div>
  <div style="width:28px;height:18px;background:#3a6ac8"></div>
  <div style="width:28px;height:18px;background:#5aa8dc"></div>
</div>

</body>
</html>
```